Event Graphics for a Summer Camp for Middle School and High School Students

I need graphics designed for our summer camps event. These camps are for teenagers, 6-12th grades. Primary graphic design is for a 11x17 poster but will also need the images resized for:
-social media
-16x9 title slide
- a postcard size
Graphic should include the following:
-Main Title: RV Pathlight presents . . . Summer Camp
-Dates: Kindle - June 3-7, High School - June 8-12, Middle School - June 22-26
-Register at RVPathlight.com
-Maple Crest Retreat Center, Deadwood, SD
-For each camp, include name and headshot of speaker: Kindle: Tom Wakeley (black jacket photo), High: Luis Ortega (hispanic man), Middle: Barrington Pope (tan shirt). Gave some options for headshots. Use what works best for cropping.
-Include RV Pathlight logo
-Event Graphic should be attractive to teenagers. Open to ideas
My graphic design experience is limited. I will need help receiving the files I need in the various sizes. Thank you.

```html
<!DOCTYPE html>
<html lang="en">
<head>
<meta charset="utf-8">
<title>RV Pathlight Summer Camp</title>
<link rel="stylesheet" href="https://fonts.googleapis.com/css2?family=Kanit:wght@300;400;500;600&family=Leckerli+One&display=swap">
<style>
  :root {
    --sky: #2fbcec;
    --sky-light: #5fd0f4;
    --sky-deep: #1da7dc;
    --sand: #f7b936;
    --sand-deep: #eea52a;
    --white: #ffffff;
    --purple: #4a2b8c;
    --green: #2a7d5e;
    --green-bright: #2f9f7c;
    --yellow: #ffd23f;
    --orange: #f39a1c;
    --ring: #38a7e6;
    --palm: #3f9d7a;
  }
  * { margin: 0; padding: 0; box-sizing: border-box; }
  html, body { width: 776px; height: 1200px; overflow: hidden; background: var(--sand); }
  .poster {
    position: relative;
    width: 776px;
    height: 1200px;
    overflow: hidden;
    font-family: "Kanit", sans-serif;
  }
  .backdrop { position: absolute; inset: 0; }

  .brand-tab {
    position: absolute;
    left: 300px; top: 0;
    width: 176px; height: 146px;
    background: var(--white);
    border-radius: 0 0 88px 88px;
    display: flex; align-items: center; justify-content: center; gap: 8px;
    padding-top: 10px;
  }
  .brand-dot { width: 14px; height: 14px; border-radius: 50%; background: var(--purple); }
  .brand-name { font-weight: 600; font-size: 22px; color: var(--purple); line-height: 1; }

  .title-diamond { position: absolute; left: 138px; top: 222px; width: 500px; height: 500px; }

  .presents {
    position: absolute; top: 322px; left: 0; width: 100%;
    text-align: center; font-size: 30px; font-weight: 400; color: var(--purple);
  }
  .title-summer, .title-camp {
    position: absolute; left: 0; width: 100%; text-align: center;
    font-family: "Leckerli One", cursive; line-height: 1; font-weight: 400;
  }
  .title-summer {
    top: 395px; font-size: 132px; color: var(--yellow);
    transform: rotate(-8deg);
    text-shadow: 0 4px 0 var(--orange);
  }
  .title-camp {
    top: 530px; font-size: 118px; color: var(--green-bright);
    transform: rotate(-8deg); padding-left: 70px;
  }

  .venue {
    position: absolute; top: 752px; left: 0; width: 100%;
    text-align: center; font-size: 27px; font-weight: 500; color: var(--green);
    white-space: nowrap;
  }
  .camp-dates { position: absolute; top: 806px; left: 104px; display: flex; }
  .camp-date {
    border-left: 2px solid var(--white);
    padding: 4px 0 4px 28px;
    color: var(--green); font-size: 21px; line-height: 1.35; font-weight: 400;
  }
  .camp-date:nth-child(1) { width: 180px; }
  .camp-date:nth-child(2) { width: 212px; }

  .speakers-label {
    position: absolute; top: 976px; left: 129px;
    font-size: 21px; color: var(--green); font-weight: 400;
  }
  .speaker { position: absolute; top: 906px; width: 140px; text-align: center; }
  .speaker-photo {
    width: 134px; height: 134px; margin: 0 auto; border-radius: 50%;
    border: 7px solid var(--white);
  }
  .speaker-name {
    margin-top: 20px; font-size: 16px; font-weight: 600; color: var(--green);
    white-space: nowrap;
  }
  .speaker-camp { margin-top: 8px; font-size: 16px; font-weight: 400; color: var(--green); }
  .speaker--kindle { left: 252px; }
  .speaker--kindle .speaker-photo { background: radial-gradient(circle at 50% 45%, #6a7fa3, #1b2333 70%); }
  .speaker--high { left: 394px; }
  .speaker--high .speaker-photo { background: radial-gradient(circle at 50% 45%, #c9a48a, #55663e 75%); }
  .speaker--middle { left: 536px; }
  .speaker--middle .speaker-photo { background: radial-gradient(circle at 50% 50%, #b58d6c, #4e4a46 75%); }

  .register-bar {
    position: absolute; left: 0; bottom: 0; width: 100%; height: 34px;
    background: var(--sand-deep);
    display: flex; align-items: center; justify-content: center;
    color: var(--white); font-size: 13px; font-weight: 300;
  }
</style>
</head>
<body>
<main class="poster">
  <svg class="backdrop" width="776" height="1200" viewBox="0 0 776 1200">
    <defs>
      <linearGradient id="palmFade" x1="0" y1="0" x2="0" y2="1">
        <stop offset="0" stop-color="#f5a623" stop-opacity="0.55"/>
        <stop offset="1" stop-color="#f5a623" stop-opacity="0.25"/>
      </linearGradient>
    </defs>
    <rect class="sky" width="776" height="1200" fill="var(--sky)"/>
    <path class="wave wave--light" d="M0 120 Q100 90 200 120 T400 120 T600 120 T800 120 V200 H0Z" fill="var(--sky-light)" opacity="0.5"/>
    <path class="wave wave--light" d="M0 200 Q100 170 200 200 T400 200 T600 200 T800 200 V280 H0Z" fill="var(--sky-light)" opacity="0.5"/>
    <path class="wave wave--deep" d="M0 330 Q120 300 240 330 T480 330 T720 330 T840 330 V420 H0Z" fill="var(--sky-deep)" opacity="0.6"/>
    <path class="shore" d="M0 620 Q180 560 330 520 Q520 470 640 430 Q720 405 776 395 V1200 H0Z" fill="var(--sand)"/>
    <path class="shore-edge" d="M0 620 Q180 560 330 520 Q520 470 640 430 Q720 405 776 395" fill="none" stroke="var(--white)" stroke-width="4" opacity="0.8"/>
    <g role="img" aria-label="Faint palm tree silhouettes on the sand">
      <ellipse cx="80" cy="1060" rx="150" ry="110" fill="url(#palmFade)"/>
      <ellipse cx="690" cy="930" rx="140" ry="170" fill="url(#palmFade)"/>
    </g>
    <g role="img" aria-label="Green palm leaves framing the upper corners">
      <ellipse cx="40" cy="310" rx="110" ry="150" fill="var(--palm)" opacity="0.85"/>
      <ellipse cx="730" cy="150" rx="110" ry="130" fill="var(--palm)" opacity="0.85"/>
    </g>
  </svg>

  <div class="brand-tab">
    <span class="brand-dot"></span>
    <span class="brand-name">RV Pathlight</span>
  </div>

  <svg class="title-diamond" viewBox="0 0 500 500" aria-hidden="true">
    <rect x="85" y="85" width="330" height="330" rx="36" transform="rotate(45 250 250)" fill="var(--ring)"/>
    <rect x="95" y="95" width="310" height="310" rx="30" transform="rotate(45 250 250)" fill="var(--orange)"/>
    <rect x="103" y="103" width="294" height="294" rx="26" transform="rotate(45 250 250)" fill="var(--white)"/>
  </svg>

  <p class="presents">Presents</p>
  <h1>
    <span class="title-summer">Summer</span>
    <span class="title-camp">Camp</span>
  </h1>

  <p class="venue">Maple Crest Retreat Center, Deadwood, SD</p>
  <div class="camp-dates">
    <div class="camp-date">Kindle<br>June 3-7</div>
    <div class="camp-date">High School<br>June 8-12</div>
    <div class="camp-date">Middle School<br>June 22-26</div>
  </div>

  <p class="speakers-label">Speakers</p>
  <div class="speaker speaker--kindle">
    <div class="speaker-photo" role="img" aria-label="Headshot of Tom Wakeley in a black jacket"></div>
    <p class="speaker-name">Tom Wakeley</p>
    <p class="speaker-camp">(Kindle)</p>
  </div>
  <div class="speaker speaker--high">
    <div class="speaker-photo" role="img" aria-label="Headshot of Luis Ortega"></div>
    <p class="speaker-name">Luis Ortega</p>
    <p class="speaker-camp">(High Sch)</p>
  </div>
  <div class="speaker speaker--middle">
    <div class="speaker-photo" role="img" aria-label="Photo of Barrington Pope"></div>
    <p class="speaker-name">Barrington Pope</p>
    <p class="speaker-camp">(Middle Sch)</p>
  </div>

  <footer class="register-bar">Register at RVPathlight.com</footer>
</main>
</body>
</html>
```